A new company focused on starting and investing in transformative businesses.

We need a simple and clean website with a few pages. we like larkmeadow.com as a starting point. we want the landing page to be very simple with an option to click through on the top right into INVESTOR LOGIN. then we want to be able to scroll down to see more about our company.

Target Market(s)

professional

Coding

Coded - Design and coding required

Number of Pages Required

2 page

Font styles to use
Serif
Sans Serif

Requirements
Must have
• HALVERN BUILDERS logo (attached as a file) on the top with INVESTOR LOGIN as a click through on the right. Please model the click through from larkmeadow.com. The description (also written in attached file) should be on the landing page. we do not want to have to scroll to read the description.

Then we can scroll down to read more about Halvern including the mission and the two types of businesses. More is detailed on the attached file called "Halvern Website Syntax"
Should not have
• should not be slow loading with lots of fancy graphics. should not be busy and with too many colors.

```html
<!DOCTYPE html>
<html lang="en">
<head>
<meta charset="utf-8">
<title>Halvern Builders</title>
<link href="https://fonts.googleapis.com/css2?family=Poppins:wght@400;500;600&display=swap" rel="stylesheet">
<style>
  :root {
    --brand-blue: #02569e;
    --accent-blue: #3a8de0;
    --ink: #1f2228;
    --muted: #9a9ca3;
    --white: #ffffff;
    --hero-top: #c9d5e3;
    --hero-mid: #8fa3bb;
    --hero-deep: #2d4a6e;
  }
  * { box-sizing: border-box; margin: 0; padding: 0; }
  html, body {
    width: 768px; height: 1200px; overflow: hidden;
    background: var(--white);
    font-family: "Poppins", sans-serif;
  }
  .page {
    position: absolute; left: 0; top: 145px;
    width: 768px; height: 910px;
  }
  /* Hero */
  .hero {
    position: absolute; left: 0; top: 0; width: 768px; height: 365px; overflow: hidden;
  }
  .hero-photo {
    position: absolute; inset: 0;
    background:
      radial-gradient(ellipse at 75% 55%, rgba(120,150,185,0.55), transparent 60%),
      radial-gradient(ellipse at 20% 30%, rgba(225,232,242,0.8), transparent 55%),
      linear-gradient(160deg, var(--hero-top) 0%, var(--hero-mid) 55%, var(--hero-deep) 100%);
  }
  .brand {
    position: absolute; left: 58px; top: 26px;
    display: flex; align-items: center; gap: 7px;
    color: var(--brand-blue); font-weight: 500; font-size: 12px; line-height: 13px; letter-spacing: 0.3px;
  }
  .brand-mark { width: 22px; height: 26px; background: var(--brand-blue); }
  .btn {
    position: absolute; display: flex; align-items: center; justify-content: center;
    width: 85px; height: 20px; border-radius: 10px;
    background: var(--brand-blue); color: var(--white);
    font-size: 7px; font-weight: 500; text-decoration: none;
  }
  .btn-login { left: 616px; top: 29px; }
  .btn-start { left: 341px; top: 257px; }
  .hero-title {
    position: absolute; left: 0; top: 140px; width: 768px;
    text-align: center; font-size: 21px; font-weight: 500; line-height: 31px; color: var(--ink);
  }
  .hero-title .highlight { color: var(--brand-blue); }
  /* About */
  .mission {
    position: absolute; left: 53px; top: 404px; width: 334px; height: 252px;
  }
  .mission svg { position: absolute; inset: 0; }
  .mission-title {
    position: absolute; left: 0; top: 52px; width: 332px; text-align: center;
    color: var(--white); font-size: 22px; font-weight: 500;
  }
  .mission-rule {
    position: absolute; left: 97px; top: 82px; width: 79px; height: 2px; background: var(--accent-blue);
  }
  .mission-text {
    position: absolute; left: 30px; top: 106px; width: 272px; text-align: center;
    color: var(--white); font-size: 14.5px; line-height: 22px; font-weight: 500;
  }
  .pillars { position: absolute; left: 420px; top: 436px; width: 300px; }
  .pillar-title { color: var(--brand-blue); font-size: 20px; font-weight: 600; line-height: 26px; }
  .pillar-text { color: var(--muted); font-size: 10.3px; line-height: 15.3px; margin-top: 2px; }
  .pillar + .pillar { margin-top: 2px; }
  /* Footer */
  .footer {
    position: absolute; left: 0; top: 757px; width: 768px; height: 153px; background: var(--brand-blue);
  }
  .footer .brand { left: 154px; top: 46px; color: var(--white); font-size: 14px; line-height: 15px; }
  .footer .brand-mark { background: var(--white); width: 26px; height: 30px; }
  .footer-contact {
    position: absolute; left: 489px; top: 38px; color: var(--white); font-size: 12.5px; line-height: 17px; font-weight: 500;
  }
  .footer-rule { position: absolute; left: 31px; top: 122px; width: 676px; height: 2px; background: var(--white); }
  .copyright {
    position: absolute; left: 0; top: 131px; width: 768px; text-align: center; color: var(--white); font-size: 8px;
  }
</style>
</head>
<body>
<main class="page">
  <header class="hero">
    <div class="hero-photo" role="img" aria-label="Blurred photo of a businessman reviewing charts on a clipboard with a pen"></div>
    <div class="brand"><span class="brand-mark"></span><span>HALVERN<br>BUILDERS</span></div>
    <a class="btn btn-login" href="#">Investor Login</a>
    <h1 class="hero-title">Halvern Builders is an entrepreneurial<br>firm focused on building and growing<br><span class="highlight">transformational companies</span></h1>
    <a class="btn btn-start" href="#">Get Started</a>
  </header>

  <section class="mission">
    <svg width="334" height="252" viewBox="0 0 334 252" aria-hidden="true">
      <path d="M30,0 L296,12 Q318,14 322,40 L332,190 Q334,238 285,240 L30,250 Q0,251 0,220 L0,32 Q0,0 30,0 Z" fill="var(--brand-blue)"/>
    </svg>
    <h2 class="mission-title">Our mission</h2>
    <div class="mission-rule"></div>
    <p class="mission-text">Our mission is to build meaningful businesses that create enduring value by impacting people in a measurable way.</p>
  </section>

  <section class="pillars">
    <div class="pillar">
      <h3 class="pillar-title">Ground Up</h3>
      <p class="pillar-text">Our ground up business applies a proven analytic process to identify value edge, a form of competitive advantage. We architect transformational companies and are deliberate in creating the foundation necessary to lead an industry.</p>
    </div>
    <div class="pillar">
      <h3 class="pillar-title">Special Opportunities</h3>
      <p class="pillar-text">We partner with exceptional teams that create value by transforming lives. Our investment focus includes large companies and spin-outs.</p>
    </div>
  </section>

  <footer class="footer">
    <div class="brand"><span class="brand-mark"></span><span>HALVERN<br>BUILDERS</span></div>
    <p class="footer-contact">Halvern Builders<br>For media inquiries, please contact<br>morgan@halvernbuilders.com</p>
    <div class="footer-rule"></div>
    <p class="copyright">© 2020 all rights reserved</p>
  </footer>
</main>
</body>
</html>
```